TVRB web site redesign

Meridale Linkworks Provisioning service (TVRB) is a diverse technology company specialising in design and installation of fibre optics, network convergence and building services, for commercial clients in Australia, we required a new design of our website to attract new clients, generate sales leads, and provide information about our services to the market. The site and should have a new technology look and feel and be designed in word press. our branding colour is blue.

Target Market(s)

New developments, Construction organisations, Commercial end users, IT managers, Consultants.

Industry/Entity Type

It Company

Number of Pages Required

5+ page

Font styles to use
Sans Serif

Colors
0292cd
3176b5

Requirements
Must have
• key pages.
• Home page with some sizzle, automated pictures running through, I like the look of this competitor website http://www.lumacrest.com.au/ good clean menus and easy to navigate.
• Services page our key services are Fibre optics, Security, Building services,Electrical. I would like the same page layout (Design) for all our services, with a find out more link on each page, manly picture driven with text around our key messaging.
• About us page with space for company profile and directors pictures, bio and contact information.
• Certifications / Accreditations page with have over 20 certifications on different products from suppliers, and a number of licences from governing bodies.
• Current and past projects page with case studies and customer outcomes
• Contact us page with options around what services they require more information on, please keep in mind the site is around generating sales Leeds and being seen as an industry expert.
Nice to have
• RSS feeds, Linked in link, to be placed within the design, Consistent TVRB branding,Same colour blue as our logo Document library for education information, white papers, presentations etc,
• a new technology look and feel, mobile friendly.
Should not have
• boring layout, move away from our cuurent website http://www.tvrbgroup.com.au/
• no e eCommerce store required.

```html
<!DOCTYPE html>
<html lang="en">
<head>
<meta charset="utf-8">
<title>TVRB — Meridale Linkworks Provisioning service</title>
<link href="https://fonts.googleapis.com/css2?family=Open+Sans:wght@400;600;700&display=swap" rel="stylesheet">
<style>
:root{
  --blue:#0292cd;
  --blue-dark:#3176b5;
  --nav:#1b5f99;
  --ink:#333;
  --muted:#666;
  --line:#dcdcdc;
  --panel:#f2f2f2;
  --footer:#3a3a3a;
  --footer-deep:#2c2c2c;
  --footer-base:#1f1f1f;
  --accent:#e07b00;
  --red:#d33;
}
*{box-sizing:border-box;margin:0;padding:0}
html,body{width:1200px;height:2706px;overflow:hidden}
body{position:relative;background:#fff;font-family:"Open Sans",Arial,sans-serif;color:var(--ink);font-size:13px;line-height:1.45}
.abs{position:absolute}
p{color:var(--muted)}

/* header */
.brand{left:175px;top:22px;display:flex;align-items:center;gap:12px}
.brand-mark{width:44px;height:44px;background:var(--blue)}
.brand-name{font-size:54px;font-weight:700;color:var(--blue);letter-spacing:2px;line-height:1}
.brand-sub{left:175px;top:92px;width:190px;font-size:9px;color:var(--blue);text-transform:uppercase;line-height:1.2}
.phone{left:557px;top:76px;display:flex;align-items:center;gap:10px;font-size:26px;font-weight:700;color:var(--blue-dark)}
.account-links{left:782px;top:10px;display:flex;gap:26px;font-size:12px;color:#444;font-weight:600}
.account-links span{display:flex;align-items:center;gap:7px}
.search{left:810px;top:82px;display:flex}
.search .field-box{width:135px;height:24px;border:1px solid #bbb;font-size:11px;padding:3px 6px;color:#888}
.search .go{width:60px;height:24px;background:#333;color:#fff;font-size:11px;font-weight:600;text-align:center;line-height:24px}

.main-nav{left:0;top:130px;width:1200px;height:36px;background:var(--nav)}
.main-nav ul{list-style:none;display:flex;gap:36px;margin-left:357px;height:36px;align-items:center}
.main-nav li{color:#fff;font-size:13px;font-weight:600}

/* hero */
.hero-photo{left:0;top:166px;width:1200px;height:360px;background:linear-gradient(120deg,#2b3b4a 0%,#566574 35%,#8c9aa3 60%,#3b4a56 100%)}
.hero-caption{left:0;top:384px;width:1200px;height:96px;background:rgba(0,0,0,.35)}
.hero-title{left:218px;top:398px;font-size:26px;line-height:1.2;color:#fff;font-weight:700;letter-spacing:.5px}
.hero-sub{left:218px;top:442px;font-size:14px;color:#fff}
.dots{left:585px;top:505px;display:flex;gap:6px}
.dots i{width:11px;height:11px;background:#fff;opacity:.6;display:block}
.dots i:first-child{opacity:1}

/* feature boxes */
.feature{top:557px;width:272px;height:240px;border:1px solid var(--line);background:#fff}
.feature-head{height:38px;background:var(--blue);color:#fff;display:flex;align-items:center;justify-content:center;gap:10px;font-size:15px;font-weight:600}
.feature-head svg{width:20px;height:20px}
.feature-img{margin:10px 12px 0;height:78px;background:linear-gradient(135deg,#5b6f83,#b8c3cc)}
.feature p{margin:8px 14px 0;font-size:11px;line-height:1.35;height:58px}
.btn{background:var(--blue-dark);color:#fff;font-size:10px;font-weight:600;padding:4px 12px;display:inline-block}
.feature .btn{position:absolute;right:14px;bottom:12px}

/* welcome */
.welcome h2{left:181px;top:862px;font-size:28px;font-weight:400;color:#222}
.welcome h2 b{color:var(--blue);font-weight:600}
.welcome p{left:181px;top:915px;width:545px;font-size:11px;line-height:1.4}
.welcome .more{left:670px;top:995px;font-size:11px;color:var(--accent);font-weight:600}
.welcome-img{left:754px;top:858px;width:265px;height:160px;background:linear-gradient(135deg,#33648f,#9fb9cf 60%,#dce6ee);border:3px solid #e6e6e6}

/* tabs */
.tabs{left:181px;top:1050px;width:838px;height:225px;background:var(--panel);border:1px solid var(--line)}
.tab-row{display:flex;height:46px;background:#fff;border-bottom:1px solid var(--line)}
.tab-row span{width:122px;display:flex;align-items:center;justify-content:center;font-size:13px;color:#333;border-right:1px solid var(--line);background:#f7f7f7}
.tab-row span.active{background:var(--blue);color:#fff;font-weight:600}
.thumbs{display:flex;gap:22px;margin:42px 0 0 68px}
.thumbs div{width:118px;height:85px;border:3px solid #fff;box-shadow:0 0 0 1px #ccc}

/* about + form */
.about h2{left:330px;top:1306px;width:270px;text-align:center;font-size:20px;font-weight:600;letter-spacing:1px;color:#222}
.about p{font-size:11px;text-align:center;width:270px;line-height:1.4;left:330px}
.about .btn{left:540px;top:1638px}
.quick{left:627px;top:1299px;width:392px;height:372px;background:var(--panel);border:1px solid var(--line)}
.quick h3{text-align:center;color:var(--blue);font-size:20px;font-weight:600;margin-top:16px}
.field{display:flex;align-items:flex-start;margin:0 0 12px 28px;font-size:11px;font-weight:600}
.field label{width:92px;padding-top:5px}
.field span{width:240px;height:28px;background:#fff;border:1px solid #ccc;display:block}
.field span.tall{height:96px}
.quick .submit{display:block;margin:14px 0 0 120px;width:240px;height:30px;background:var(--blue-dark);color:#fff;text-align:center;line-height:30px;font-size:11px;font-weight:700}

/* partners */
.partners h2{left:0;top:1710px;width:1200px;text-align:center;font-size:28px;font-weight:600;color:#222}
.partners p{left:0;top:1758px;width:1200px;text-align:center;font-size:12px}
.badges{left:205px;top:1818px;display:flex;gap:52px}
.badges div{width:118px;height:44px;background:#cfcfcf}
.badges div:nth-child(2n){border-radius:22px;background:#bdbdbd}

/* testimonials */
.customers h2{left:190px;top:1966px;font-size:26px;font-weight:600;color:#222}
.quote{width:400px;display:flex;gap:20px}
.avatar{width:54px;height:54px;border-radius:50%;background:radial-gradient(circle at 50% 40%,#c9b8a6,#7d8996);flex:none}
.quote p{font-size:11px;line-height:1.35}
.quote .who{font-size:10px;margin-top:8px;color:#555}
.quote .who b{color:var(--red);font-weight:600}

/* footer */
.footer{left:0;top:2292px;width:1200px;height:268px;background:var(--footer)}
.footer-col{top:2305px;color:#ddd;font-size:11px}
.footer-col h4{color:#fff;font-size:12px;font-weight:600;margin-bottom:10px}
.footer-col li{list-style:none;margin-bottom:6px}
.news li{display:flex;gap:10px;margin-bottom:10px;width:230px}
.news i{width:54px;height:34px;background:linear-gradient(135deg,#566a7c,#9aa9b6);flex:none;display:block}
.news span{line-height:1.3;font-size:10px}
.viewall{left:0;top:2535px;width:1200px;text-align:center;color:#fff;font-size:11px}
.newsletter{left:0;top:2560px;width:1200px;height:108px;background:var(--footer-deep)}
.news-tag{left:0;top:2568px;width:1200px;text-align:center;color:#ddd;font-size:11px}
.nl-row{left:320px;top:2588px;display:flex;align-items:center;gap:12px}
.nl-row strong{color:#fff;font-size:20px;font-weight:600;letter-spacing:1px}
.nl-row span.input{width:290px;height:26px;background:#fff;font-size:11px;color:#999;padding:5px 8px}
.nl-row span.go{width:80px;height:26px;background:var(--blue);color:#fff;font-size:12px;font-weight:700;text-align:center;line-height:26px}
.follow{left:470px;top:2632px;display:flex;align-items:center;gap:5px;color:#fff;font-size:11px;font-weight:600}
.follow i{width:16px;height:16px;background:var(--blue-dark);display:block}
.follow i:nth-child(odd){background:#777}
.copyright{left:0;top:2668px;width:1200px;height:38px;background:var(--footer-base);color:#ccc;text-align:center;font-size:11px;line-height:38px}
</style>
</head>
<body>

<header>
  <div class="abs brand"><span class="brand-mark"></span><span class="brand-name">TVRB</span></div>
  <div class="abs brand-sub">Meridale Linkworks Provisioning service</div>

  <div class="abs phone">
    <svg width="22" height="26" viewBox="0 0 24 24"><path fill="#3176b5" d="M6.6 10.8a15 15 0 0 0 6.6 6.6l2.2-2.2c.3-.3.7-.4 1-.2 1.1.4 2.3.6 3.6.6.6 0 1 .4 1 1V20c0 .6-.4 1-1 1A17 17 0 0 1 3 4c0-.6.4-1 1-1h3.5c.6 0 1 .4 1 1 0 1.3.2 2.5.6 3.6.1.3 0 .7-.2 1z"/></svg>
    1300 555 019
  </div>

  <div class="abs account-links">
    <span><svg width="14" height="14" viewBox="0 0 16 16"><circle cx="8" cy="5" r="3.5" fill="#444"/><path d="M1 16c0-4 3-6 7-6s7 2 7 6z" fill="#444"/></svg>MY ACCOUNT</span>
    <span><svg width="16" height="14" viewBox="0 0 18 16"><path d="M0 1h3l2 9h10l2-7H5" fill="none" stroke="#444" stroke-width="1.6"/><circle cx="7" cy="14" r="1.5" fill="#444"/><circle cx="14" cy="14" r="1.5" fill="#444"/></svg>MY CART</span>
  </div>

  <div class="abs search"><span class="field-box">Keywords</span><span class="go">Search</span></div>

  <nav class="abs main-nav">
    <ul><li>HOME</li><li>ABOUT US</li><li>SERVICES</li><li>ISP</li><li>RECENT PROJECTS</li><li>BLOG</li><li>CONTACT US</li></ul>
  </nav>
</header>

<section class="hero-block">
  <div class="abs hero-photo" role="img" aria-label="Technician splicing fibre optic cables in a network cabinet"></div>
  <div class="abs hero-caption"></div>
  <h1 class="abs hero-title">LORM IPSUM DOLOR SIT AMET, CONSECTETUR ADIPISCING</h1>
  <p class="abs hero-sub">Lorem ipsum dolor sit amet, consectetur adipiscing elit, sed diam nonummy nibh euismod tincidunt ut laoreet dolore.</p>
  <div class="abs dots"><i></i><i></i><i></i><i></i><i></i></div>
</section>

<section class="features">
  <div class="abs feature" style="left:181px">
    <div class="feature-head"><svg viewBox="0 0 24 24"><circle cx="8" cy="8" r="3.5" fill="#fff"/><circle cx="16" cy="8" r="3.5" fill="#fff"/><path d="M1 20c0-4 3-6 7-6s7 2 7 6zM11 20c0-4 3-6 6-6s6 2 6 6z" fill="#fff"/></svg>WHO WE ARE</div>
    <div class="feature-img" role="img" aria-label="Team meeting in an office"></div>
    <p>Lorem ipsum dolor sit amet, consectetur adipiscing elit. Sed diam nonummy in convallis gravida neque. Nulla gravida nisi libero metus.</p>
    <span class="btn">read more</span>
  </div>
  <div class="abs feature" style="left:468px">
    <div class="feature-head"><svg viewBox="0 0 24 24"><rect x="3" y="5" width="18" height="13" fill="none" stroke="#fff" stroke-width="2"/><path d="M8 21h8" stroke="#fff" stroke-width="2"/></svg>WHAT WE DO</div>
    <div class="feature-img" role="img" aria-label="Engineer working at a data cabinet"></div>
    <p>Lorem ipsum dolor sit amet, consectetur adipiscing elit. Sed diam nonummy in convallis gravida neque. Nulla gravida nisi libero metus.</p>
    <span class="btn">read more</span>
  </div>
  <div class="abs feature" style="left:754px">
    <div class="feature-head"><svg viewBox="0 0 24 24"><circle cx="12" cy="12" r="4" fill="none" stroke="#fff" stroke-width="2"/><path d="M12 2v4M12 18v4M2 12h4M18 12h4M5 5l3 3M16 16l3 3M5 19l3-3M16 8l3-3" stroke="#fff" stroke-width="2"/></svg>OUR SERVICES</div>
    <div class="feature-img" role="img" aria-label="Glowing fibre optic strands" style="background:linear-gradient(135deg,#0a2a55,#2a8fd0)"></div>
    <p style="color:#333">Commercial Security Systems<br>Data &amp; Fibre Installations<br>Information Communication &amp; Technology<br>Electrical Fits Out</p>
    <span class="btn">read more</span>
  </div>
</section>

<section class="welcome">
  <h2 class="abs">Wecome to <b>TVRB.com</b></h2>
  <p class="abs">Lorem ipsum dolor sit amet, consectetur adipiscing elit. Sed diam nonummy in convallis gravida neque. Nulla gravida vestibulum metus a accumsan, aliquam in sagittis ut. Sollicitudin sed massa ut enim varius. Curabitur tempus vehicula mi vestibulum volutpat malesuada erat vestibulum. Sed aliquam dolor at dolor consequat gravida. Fusce tempus tempus nisi, feugiat vit amet. Tincidunt ut leo. Nam semper ornare amet. Lorem ipsum dolor sit amet, consectetur adipiscing elit.</p>
  <span class="abs more">Read more</span>
  <div class="abs welcome-img" role="img" aria-label="Business professional in a suit speaking on the phone"></div>
</section>

<section class="abs tabs">
  <div class="tab-row"><span class="active">FEATURED</span><span>NEW ARRIVALS</span><span>ON SALE</span></div>
  <div class="thumbs">
    <div role="img" aria-label="Hands assembling network hardware" style="background:linear-gradient(135deg,#6f8aa5,#d1dbe3)"></div>
    <div role="img" aria-label="Server room corridor" style="background:linear-gradient(135deg,#1f4b7a,#6aa3d4)"></div>
    <div role="img" aria-label="Blue technology circuit graphic" style="background:linear-gradient(135deg,#0b3e78,#3a9ce0)"></div>
    <div role="img" aria-label="Bundle of blue fibre cables" style="background:linear-gradient(135deg,#1c6fb8,#8fc8ee)"></div>
    <div role="img" aria-label="Group of colleagues in an office" style="background:linear-gradient(135deg,#5f6f82,#c5ccd4)"></div>
  </div>
</section>

<section class="about">
  <h2 class="abs">ABOUT US</h2>
  <p class="abs" style="top:1348px">Lorem ipsum dolor sit amet, consectetur adipiscing elit. Sed diam nonummy in convallis gravida neque. Nulla gravida vestibulum metus a accumsan, aliquam in sagittis ut. Sollicitudin sed massa ut enim varius. Curabitur tempus vehicula mi vestibulum volutpat malesuada erat.</p>
  <p class="abs" style="top:1470px">Lorem ipsum dolor sit amet consectetur adipiscing elit sed diam nonummy incorvalis gravida neque, nulla gravida vestibulum metus a accumsan, aliquam in sagittis ut. Sollicitudin sed massa ut enim varius, curabitur tempus vehicula mi vestibulum volutpat malesuada erat vestibulum.</p>
  <span class="abs btn">read more</span>

  <div class="abs quick" aria-label="Quick question">
    <h3>QUICK QUESTION</h3>
    <div style="margin-top:26px">
      <div class="field"><label>Name</label><span></span></div>
      <div class="field"><label>Phone</label><span></span></div>
      <div class="field"><label>Email</label><span></span></div>
      <div class="field"><label>Message</label><span class="tall"></span></div>
    </div>
    <span class="submit">SUBMIT</span>
  </div>
</section>

<section class="partners">
  <h2 class="abs">Our Partners</h2>
  <p class="abs">Lorem ipsum dolor sit amet, consectetur adipiscing elit. Sed diam nonummy incorvalis gravida neque.</p>
  <div class="abs badges"><div></div><div></div><div></div><div></div><div></div></div>
</section>

<section class="customers">
  <h2 class="abs">What Our Customer Says</h2>
  <div class="abs quote" style="left:195px;top:2025px"><span class="avatar" role="img" aria-label="Customer portrait"></span><div><p>Lorem ipsum dolor sit amet, consectetur adipiscing elit. Sed diam nonummy incorvalis gravida neque. Nulla gravida vestibulum metus a accumsan aliquam in.</p><p class="who"><b>Mara Keller</b>, Marketing , Sinika</p></div></div>
  <div class="abs quote" style="left:627px;top:2025px"><span class="avatar" role="img" aria-label="Customer portrait"></span><div><p>Lorem ipsum dolor sit amet, consectetur adipiscing elit. Sed diam nonummy incorvalis gravida neque. Nulla gravida vestibulum metus a accumsan aliquam in.</p><p class="who"><b>Glen Harlow</b>, IT Engineer, Westbridge</p></div></div>
  <div class="abs quote" style="left:195px;top:2133px"><span class="avatar" role="img" aria-label="Customer portrait"></span><div><p>Lorem ipsum dolor sit amet, consectetur adipiscing elit. Sed diam nonummy incorvalis gravida neque. Nulla gravida vestibulum metus a accumsan aliquam in.</p><p class="who"><b>Owen Tarrant</b>, Public Relations , New Vale</p></div></div>
  <div class="abs quote" style="left:627px;top:2133px"><span class="avatar" role="img" aria-label="Customer portrait"></span><div><p>Lorem ipsum dolor sit amet, consectetur adipiscing elit. Sed diam nonummy incorvalis gravida neque. Nulla gravida vestibulum metus a accumsan aliquam in.</p><p class="who"><b>Neil Brandt</b>, CEO, Marketing , Irelis</p></div></div>
</section>

<footer>
  <div class="abs footer"></div>
  <div class="abs footer-col" style="left:181px"><h4>MAIN MENU</h4><ul><li>Home</li><li>About Us</li><li>Services</li><li>ISP</li><li>Recent Projects</li><li>Blog</li><li>Contact Us</li></ul></div>
  <div class="abs footer-col news" style="left:357px"><h4>LATEST NEWS &amp; UPDATES</h4><ul>
    <li><i></i><span>January, 13th 2014 Lorem ipsum dolor sit amet consectetur elit</span></li>
    <li><i></i><span>February, 07th 2014 Lorem ipsum dolor sit amet consectetur elit</span></li>
    <li><i></i><span>March, 11th 2014 Lorem ipsum dolor sit amet consectetur elit</span></li>
    <li><i></i><span>March, 26th 2014 Lorem ipsum dolor sit amet consectetur elit</span></li>
  </ul></div>
  <div class="abs footer-col" style="left:630px"><h4>USEFULL LINKS</h4><ul><li>terms &amp; Conditions</li><li>Privacy policy</li><li>HELP</li><li>FAQs</li><li>Sitemap</li></ul></div>
  <div class="abs footer-col" style="left:805px"><h4>MY ACCOUNT</h4><ul><li>My Account</li><li>Sign In</li><li>Order Status</li><li>My Cart</li><li>My WhisList</li></ul></div>
  <div class="abs viewall">View All</div>

  <div class="abs newsletter"></div>
  <div class="abs news-tag">Receive Our News &amp; updates weekly, no worry about your details</div>
  <div class="abs nl-row"><strong>NEWSLETTER</strong><span class="input">Your email address</span><span class="go">SUBMIT</span></div>
  <div class="abs follow">FOLLOW US ON&nbsp;<i></i><i></i><i></i><i></i><i></i><i></i><i></i><i></i></div>

  <div class="abs copyright">Copyright © 2014, TVRB.com . All right reserved.</div>
</footer>

</body>
</html>
```